Corporate consulting business needs a business card

I want a professional business card.... surprise me

Updates

Reason: i dont think 2 days is enough

Target Market(s)

Corprorate and Not for Profit firms and organisations

Industry/Entity Type

Consulting

Contact Information for Business Card

Logo
Corporate Consulting Services
On Time, On Budget, Beyond Expectation
Tovan Presfield
Director
0427 31 94 62 (Larger)
tovan@tp-advisory.com.au
www.tp-advisory.com.au
include little icons beside the contact info:

- Envelope = email
- Phone = phone
- Globe = website

Font styles to use
Serif
Sans Serif

Requirements
Must have
• Professional and clean
Nice to have
• you tell me

```html
<!DOCTYPE html>
<html lang="en">
<head>
<meta charset="utf-8">
<title>TP Advisory Services – Business Card</title>
<link rel="stylesheet" href="https://fonts.googleapis.com/css2?family=Libre+Baskerville:wght@400;700&family=Lato:wght@400;700&display=swap">
<style>
  :root {
    --backdrop: #3d3d3f;
    --card: #ffffff;
    --brown: #5a3620;
    --ink: #1e1a17;
    --grey: #8d8882;
    --serif: "Libre Baskerville", Georgia, serif;
    --sans: "Lato", Arial, sans-serif;
  }
  * { box-sizing: border-box; margin: 0; padding: 0; }
  html, body { width: 1200px; height: 810px; overflow: hidden; }
  body {
    background: var(--backdrop);
    display: flex;
    align-items: center;
    justify-content: center;
    gap: 40px;
  }
  .card {
    width: 540px;
    height: 310px;
    background: var(--card);
    border-radius: 24px;
    box-shadow: 0 6px 18px rgba(0,0,0,.35);
    position: relative;
    display: flex;
    flex-direction: column;
    align-items: center;
  }
  .brand {
    display: flex;
    align-items: center;
    gap: 12px;
  }
  .brand-dot {
    width: 44px; height: 44px;
    border: 3px solid var(--brown);
    border-radius: 50%;
  }
  .brand-name {
    font-family: var(--serif);
    font-weight: 700;
    font-size: 17px;
    letter-spacing: .04em;
    text-transform: uppercase;
    color: var(--ink);
  }
  .card-front .brand { margin-top: 92px; }
  .tagline {
    margin-top: 78px;
    font-family: var(--sans);
    font-size: 15px;
    color: var(--brown);
    word-spacing: 2px;
  }
  .card-back .brand { margin-top: 46px; }
  .person { margin-top: 36px; text-align: center; }
  .person-name {
    font-family: var(--serif);
    font-size: 20px;
    letter-spacing: .05em;
    text-transform: uppercase;
    color: var(--brown);
  }
  .person-role {
    font-family: var(--sans);
    font-size: 13px;
    color: var(--grey);
    margin-top: 2px;
  }
  .contact-row {
    display: flex;
    align-items: center;
    gap: 18px;
    margin-top: 14px;
  }
  .contact {
    display: flex;
    align-items: center;
    gap: 6px;
    font-family: var(--sans);
    color: var(--grey);
    font-size: 13px;
  }
  .contact svg { fill: var(--brown); flex: none; }
  .contact-phone { font-size: 26px; color: var(--brown); }
  .contact-email { margin-top: 14px; }
</style>
</head>
<body>
  <section class="card card-front">
    <div class="brand">
      <span class="brand-dot"></span>
      <span class="brand-name">TP Advisory Services</span>
    </div>
    <p class="tagline">• On Time • On Budget • Beyond Expectation</p>
  </section>

  <section class="card card-back">
    <div class="brand">
      <span class="brand-dot"></span>
      <span class="brand-name">TP Advisory Services</span>
    </div>
    <div class="person">
      <p class="person-name">Tovan Presfield</p>
      <p class="person-role">Director</p>
    </div>
    <div class="contact-row">
      <span class="contact contact-phone">
        <svg width="20" height="20" viewBox="0 0 24 24" aria-hidden="true"><path d="M6.6 10.8a15.1 15.1 0 0 0 6.6 6.6l2.2-2.2c.3-.3.7-.4 1-.2 1.1.4 2.3.6 3.6.6.6 0 1 .4 1 1V20c0 .6-.4 1-1 1A17 17 0 0 1 3 4c0-.6.4-1 1-1h3.5c.6 0 1 .4 1 1 0 1.3.2 2.5.6 3.6.1.3 0 .7-.2 1z"/></svg>
        0427 31 94 62
      </span>
      <span class="contact contact-web">
        <svg width="14" height="14" viewBox="0 0 24 24" aria-hidden="true"><path d="M12 2a10 10 0 1 0 0 20 10 10 0 0 0 0-20zm6.9 6h-3a15.6 15.6 0 0 0-1.3-3.9A8 8 0 0 1 18.9 8zM12 4c.8 1.2 1.5 2.5 1.9 4h-3.8c.4-1.5 1.1-2.8 1.9-4zM4.3 14a8 8 0 0 1 0-4h3.4a16 16 0 0 0 0 4zm.8 2h3a15.6 15.6 0 0 0 1.3 3.9A8 8 0 0 1 5.1 16zm3-8h-3a8 8 0 0 1 4.3-3.9C8.8 5.3 8.4 6.6 8.1 8zM12 20c-.8-1.2-1.5-2.5-1.9-4h3.8c-.4 1.5-1.1 2.8-1.9 4zm2.3-6H9.7a14.7 14.7 0 0 1 0-4h4.6a14.7 14.7 0 0 1 0 4zm.3 5.9c.6-1.2 1-2.5 1.3-3.9h3a8 8 0 0 1-4.3 3.9zm1.7-5.9a16 16 0 0 0 0-4h3.4a8 8 0 0 1 0 4z"/></svg>
        www.tp-advisory.com.au
      </span>
    </div>
    <span class="contact contact-email">
      <svg width="15" height="12" viewBox="0 0 24 18" aria-hidden="true"><path d="M0 0h24v18H0zm2 2.5V16h20V2.5l-10 7z"/><path d="M2 0h20l-10 7z" fill="#fff"/></svg>
      tovan@tp-advisory.com.au
    </span>
  </section>
</body>
</html>
```